Quietude Lantern Habits book cover

Hello!
I need a 5.25x8 VNR paperback cover and ZOB audiobook square cover with the same design. (I might need a Spanish copy as well, but that should just be copy and pasting the translation after the winner is chosen, so don't worry about that for now.)
The title text should be laid out something like this:
A QUICK
WHAT, WHO, WHY, WHERE, HOW & WHEN
-----OF-----
QUIETUDE
LANTERN HABITS
The book should be about 160 pages, for the spine width.
I have attached some concepts/ideas I have for inspiration, but feel free to submit any kinds of ideas you might have. I'm open to your creativity!
~~~~~~~~
Back Sleeve Summary:
Countless studies and anecdotal reports have shown that large doses of psilocybin mushrooms can inspire breakthroughs and mystical experiences or help relieve symptoms of mental health disorders and physical ailments. However, macrodosing psychedelics doesn’t always have a practical application in our day-to-day lives.
Enter microdosing: a method of taking small amounts of psychedelics to invoke a desirable physiological response with minimal undesirable drawbacks. The practice has become more popular in recent years and is proving to be a safe and powerful approach not only to addressing an array of health concerns but also to improving general performance.
Whether you’re looking to taper off pharmaceuticals or simply improve your mood, creativity, sleep, eating habits, physical stamina, or sexual performance, this book will help you learn how microdosing could improve your overall quality of life. The information herein also doesn’t shy away from addressing more controversial topics, such as microdosing in youth or during pregnancy.
This book is intended to provide foundational knowledge of what microdosing is, who is doing it, various motivations for doing so, ideal times and protocols for practice, considerations for where to microdose, and how to go about sourcing and dosing psilocybin mushrooms. It is a carefully researched, beginner-friendly guide that weaves together concise history and research with practical application and integration of microdosing psilocybin.
Author Section (with attached photo):
Dale Pemberton earned a B.S. in Kinesiology from the University of Harwick Vale, and has furthered his studies in the fields of psychedelics, psychology, and trauma healing since 2012. He’s been exploring the benefits of psychedelics within himself for equally as long.
People interested in self help, healing, and microdosing psychedelics.

```html
<!DOCTYPE html>
<html lang="en">
<head>
<meta charset="utf-8">
<title>Quietude Lantern Habits — Book Cover</title>
<link rel="stylesheet" href="https://fonts.googleapis.com/css2?family=Montserrat:wght@500&family=Poppins:wght@800&display=swap">
<style>
  :root {
    --page: #ffffff;
    --cover-deep: #1d2c33;
    --forest-mid: #3a4c45;
    --forest-glow: #5d7a66;
    --cream: #f6e6ac;
    --white: #ffffff;
    --amber: #c99a45;
  }
  * { margin: 0; padding: 0; box-sizing: border-box; }
  html, body {
    width: 1200px; height: 1200px; overflow: hidden;
    background: var(--page);
  }
  .cover {
    position: absolute; left: 200px; top: 0;
    width: 800px; height: 1200px;
    background: var(--cover-deep);
    box-shadow: 0 0 18px rgba(0,0,0,0.35);
    overflow: hidden;
  }
  .forest-scene {
    position: absolute; inset: 0 0 360px 0;
    background:
      radial-gradient(ellipse 60% 45% at 50% 55%, var(--forest-glow) 0%, rgba(93,122,102,0) 70%),
      linear-gradient(180deg, #2c3c3b 0%, var(--forest-mid) 45%, #2d3e38 80%, var(--cover-deep) 100%);
  }
  .product-art {
    position: absolute; left: 170px; top: 265px;
    width: 460px; height: 540px;
    background:
      radial-gradient(ellipse 14% 30% at 50% 48%, rgba(201,154,69,0.85) 0%, rgba(201,154,69,0.35) 60%, rgba(201,154,69,0) 100%),
      radial-gradient(ellipse 45% 14% at 50% 88%, rgba(220,200,150,0.35) 0%, rgba(220,200,150,0) 100%);
  }
  .kicker {
    position: absolute; left: 0; right: 0; top: 56px;
    text-align: center;
    font-family: "Montserrat", sans-serif; font-weight: 500;
    font-size: 50px; letter-spacing: 7px;
    color: var(--cream);
  }
  .subtitle {
    position: absolute; left: 0; right: 0; top: 116px;
    text-align: center;
    font-family: "Poppins", sans-serif; font-weight: 800;
    font-size: 57px; line-height: 72px;
    color: var(--white);
    letter-spacing: -0.5px;
  }
  .connector {
    position: absolute; left: 315px; top: 790px;
    font-family: "Poppins", sans-serif; font-weight: 800;
    font-size: 42px; color: var(--white);
  }
  .title {
    position: absolute; left: 0; right: 0; top: 836px;
    text-align: center;
    font-family: "Poppins", sans-serif; font-weight: 800;
    font-size: 88px; line-height: 96px;
    color: var(--cream);
    letter-spacing: -1px;
  }
  .author {
    position: absolute; left: 0; right: 0; top: 1124px;
    text-align: center;
    font-family: "Poppins", sans-serif; font-weight: 800;
    font-size: 40px; color: var(--white);
  }
</style>
</head>
<body>
  <main class="cover">
    <div class="forest-scene" role="img" aria-label="Misty dark forest with tall trees and soft light"></div>
    <div class="product-art" role="img" aria-label="Glass dropper bottle holding mushrooms in amber liquid, a drop falling onto a brain with circuit lines"></div>

    <p class="kicker">A QUICK</p>
    <h2 class="subtitle">What, Who, Why,<br>Where, How &amp; When</h2>
    <p class="connector">of</p>
    <h1 class="title">Quietude<br>Lantern<br>Habits</h1>
    <p class="author">Dale Pemberton</p>
  </main>
</body>
</html>
```